Wordpress Design for my Consulting Company

We want a WordPress site created for our new business. We have created a mock-up of the content we want on the site at https://marcusdellow.example-sites.com/website-5

We are not attached to any of the pictures and just put stock stuff from wix's editor, which we don't have rights to use outside of wix.

We are NOT looking to just port this site to WordPress, we are looking for some creative ways to display the content in a more professional artistic sense.

I have included several logo files and a text file with the colors and Fonts used in the logo. We are not looking to change the logo or the colors used in the logo.

The Schedule appointment links to a page that embeds a bookingnest.example.com calendar. https://bookingnest.example.com/marcus-dellow/brightvale

The final website domain will be enterprisebrightvale.example

Enterprise brightvale is a consulting company that works directly with the business owners and leaders of small businesses between 50-200 employees. We help companies make sure they have the right technology to meet their strategic goals. We are the anti-"Computer Guy" and we focus on business outcomes NOT cool technology gadgets.

The final design should communicate business growth and success.

Target Market(s)

Business Owners of companies with 50-200 employees

Coding

Coded - Design and coding required

Number of Pages Required

1 page

Font styles to use
Serif
Other font styles liked:
• Trajan Pro Bold, Open Sans

Requirements
Must have
• Should focus on consulting rather than technology.
• Should show the customer as the hero and we are just their guide.
• Must use the logo provided and the colors and fonts in the text file provided. Any other colors and fonts must be complementary.
• The design should scale for all devices computer, iPad, or phone
Should not have
• Should not focus on technology, we are the anti-"Computer Guy" and we focus on business outcomes NOT cool technology gadgets.

```html
<!DOCTYPE html>
<html lang="en">
<head>
<meta charset="utf-8">
<title>Brightvale — Technology Advisors</title>
<link rel="stylesheet" href="https://fonts.googleapis.com/css2?family=Cinzel:wght@400;600&family=Open+Sans:wght@400;700&display=swap">
<style>
  :root {
    --ink: #33434b;
    --copper: #c8794b;
    --paper: #ffffff;
    --muted: #4a4f52;
  }
  * { margin: 0; padding: 0; box-sizing: border-box; }
  html, body { width: 1200px; height: 675px; overflow: hidden; background: var(--paper); }
  .page { position: relative; width: 1200px; height: 675px; background: var(--paper); }

  .brand { position: absolute; left: 228px; top: 16px; width: 104px; text-align: center; }
  .brand-mark { display: block; width: 46px; height: 46px; margin: 0 auto 4px; border-radius: 50%; background: var(--ink); }
  .brand-name { font-family: "Cinzel", serif; font-weight: 400; font-size: 12.5px; letter-spacing: 0.5px; color: var(--ink); }

  .main-nav { position: absolute; top: 49px; left: 685px; display: flex; gap: 0; }
  .main-nav a {
    font-family: "Open Sans", sans-serif; font-weight: 700; font-size: 8.8px;
    letter-spacing: 0.9px; text-transform: uppercase; text-decoration: none; color: var(--ink);
    margin-right: 26px; line-height: 12px;
  }
  .main-nav a:last-child { margin-right: 0; }
  .main-nav a.is-current { color: var(--copper); }

  .hero { position: absolute; left: 228px; top: 232px; }
  .hero-title {
    font-family: "Cinzel", serif; font-weight: 600; font-size: 43px; line-height: 59px;
    color: var(--ink); letter-spacing: 0.3px;
  }
  .hero-lead {
    margin-top: 6px;
    font-family: "Cinzel", serif; font-weight: 600; font-size: 16.5px;
    color: var(--ink); letter-spacing: 0.3px;
  }

  .cta { position: absolute; left: 228px; top: 406px; width: 146px; height: 35px; text-decoration: none; }
  .cta-block { position: absolute; left: 27px; top: 0; width: 118px; height: 35px; background: var(--copper); }
  .cta-label {
    position: absolute; left: 0; top: 10px;
    font-family: "Open Sans", sans-serif; font-size: 11px; letter-spacing: 0.5px; color: var(--muted);
    white-space: nowrap;
  }
  .cta-line { position: absolute; left: 120px; top: 17px; width: 20px; height: 1px; background: var(--paper); }
</style>
</head>
<body>
<div class="page">
  <header>
    <div class="brand">
      <span class="brand-mark"></span>
      <span class="brand-name">Brightvale</span>
    </div>
    <nav class="main-nav">
      <a href="#" class="is-current">Home</a>
      <a href="#">About Us</a>
      <a href="#">Team</a>
      <a href="#">Blog</a>
      <a href="#">Contact</a>
    </nav>
  </header>

  <section class="hero">
    <h1 class="hero-title">Technology Advisors That<br>"Get" Business.</h1>
    <p class="hero-lead">We help you leverage technology to create a competitive advantage.</p>
  </section>

  <a class="cta" href="https://bookingnest.example.com/marcus-dellow/brightvale">
    <span class="cta-block"></span>
    <span class="cta-label">Schedule Appoitment</span>
    <span class="cta-line"></span>
  </a>
</div>
</body>
</html>
```